Local Restaurant Needs a One Page Breakfast Menu

I own a restaurant and we are going to be starting a new breakfast service. I want a one page menu that is clean, bright, and tongue in cheek. We will only have a limited menu, so there should be plenty of space to work with. I will not want actual food pictures, but more of a cartoon style representations of food. I'd like a modern cartoon style mixed with our current 1950s theme.

Name of Restaurant: Tully's
Location: 2493 W. Larch. Hutchinson, KS 58214 - Phone: 620-555-3047 (including location is not a requirement)

Breakfast Hours: 6:30 am - 10:30 am

The two colors selected below are not required, but they are the two colors that are featured inside the dining room of the restaurant.

Industry/Entity Type

Restaurant

Colors
8667ad
acd036

Requirements
Must have
• Menu must only be one page (either standard letter or oversized - either would be ok).

Menu items:

Stuffed Omellete. Stuffing choices: cheese, peppers, jalapenos, onions, tomatoes, salsa, sour cream, green onions, sausage, bacon, ham

Tully's Blintz (thin, stuffed, pancakes): Stuffing choices: chocolate chips, Q&Zs, Talbot's Nibbles, strawberries, blueberries, raspberries, bananas, sour cream

Homemade Coffee Cake

Cinnamon Rolls

Beverages - Coffee, Soda, Milk

Prices not set (use placeholders).

```html
<!DOCTYPE html>
<html lang="en">
<head>
<meta charset="utf-8">
<title>Tully's Breakfast Menu</title>
<link rel="stylesheet" href="https://fonts.googleapis.com/css2?family=Alfa+Slab+One&family=Yellowtail&family=Kaushan+Script&family=Libre+Baskerville:wght@700&family=Roboto:ital,wght@0,400;1,400&display=swap">
<style>
  :root {
    --paper-light: #f7e6c8;
    --paper-mid: #f2d3a4;
    --paper-edge: #e9b57c;
    --blue: #3a5fd0;
    --pink: #d2399f;
    --desc-pink: #d34bb0;
  }
  html, body { margin: 0; padding: 0; overflow: hidden; }
  .menu {
    position: relative;
    width: 887px;
    height: 1200px;
    overflow: hidden;
    background: radial-gradient(ellipse at 50% 40%, var(--paper-light) 0%, var(--paper-mid) 60%, var(--paper-edge) 100%);
    font-family: "Roboto", sans-serif;
  }
  .menu > * { position: absolute; margin: 0; }
  .title {
    left: 28px; top: 22px;
    font-family: "Alfa Slab One", serif;
    font-weight: 400;
    font-size: 90px; line-height: 1;
    color: var(--blue);
    letter-spacing: 1px;
  }
  .hours {
    left: 29px; top: 120px;
    font-family: "Alfa Slab One", serif;
    font-size: 32px; line-height: 1; color: var(--pink);
  }
  .brand {
    left: 556px; top: 26px;
    font-family: "Alfa Slab One", serif;
    font-size: 66px; line-height: 1.3;
    color: var(--pink);
  }
  .flourish { left: 155px; top: 161px; width: 222px; height: 30px; border-radius: 15px; background: #4a3a30; opacity: .75; }
  .item-name {
    margin: 0;
    font-family: "Yellowtail", "Kaushan Script", cursive;
    font-weight: 400;
    font-size: 44px; line-height: 1;
    color: var(--blue);
    white-space: nowrap;
  }
  .item-note { font-family: "Roboto", sans-serif; font-style: italic; font-size: 28px; }
  .row { display: flex; align-items: center; }
  .desc {
    font-size: 22px; line-height: 31px; color: var(--desc-pink);
  }
  .price {
    margin: 0;
    font-family: "Libre Baskerville", serif; font-weight: 700;
    font-size: 38px; line-height: 1; color: var(--blue);
    white-space: nowrap;
  }
  .art { border-radius: 50%; flex: none; }
  .drink, .drink-price {
    font-family: "Libre Baskerville", serif; font-weight: 700;
    font-size: 38px; line-height: 1; color: var(--pink);
  }
</style>
</head>
<body>
<main class="menu">
  <h1 class="title">Breakfast</h1>
  <p class="hours">Hours: 6:30 am to 10:30 am</p>
  <p class="brand">Tully's</p>
  <div class="flourish" role="img" aria-label="Decorative scroll flourish"></div>

  <h2 class="item-name" style="left:28px;top:216px;">Stuffed Omellete</h2>
  <p class="desc" style="left:24px;top:259px;width:560px;">cheese, peppers, jalapenos, onions, tomatoes, salsa, sour cream, green onions, sausage, bacon, ham</p>
  <div class="art" role="img" aria-label="Cartoon stuffed omelette" style="left:600px;top:200px;width:100px;height:108px;background:linear-gradient(160deg,#f2c23c,#e0a52a 70%,#7a9a3a);"></div>
  <p class="price" style="left:717px;top:216px;">$ 00.0</p>

  <p class="price" style="left:32px;top:354px;">$ 00.0</p>
  <div class="art" role="img" aria-label="Cartoon stack of pancakes with syrup" style="left:100px;top:392px;width:96px;height:70px;background:linear-gradient(180deg,#6b3e1e,#d98a44);"></div>
  <h2 class="item-name" style="left:210px;top:350px;">Tully's Blintz <span class="item-note">(thin, stuffed, pancakes)</span></h2>
  <p class="desc" style="left:209px;top:405px;width:640px;">chocolate chips, Q&amp;Zs, Talbot's Nibbles,strawberries, blueberries, raspberries, bananas, sour cream</p>

  <div class="row" style="left:28px;top:487px;height:70px;">
    <h2 class="item-name">Homemade Coffee Cake</h2>
    <div class="art" role="img" aria-label="Cartoon slice of coffee cake on a plate" style="margin-left:16px;width:131px;height:70px;background:linear-gradient(180deg,#8a5a2e,#f4e8d0 45%,#b6d35a);"></div>
    <p class="price" style="margin-left:24px;">$ 00.0</p>
  </div>

  <div class="row" style="left:28px;top:566px;height:73px;">
    <h2 class="item-name">Cinnamon Rolls</h2>
    <div class="art" role="img" aria-label="Cartoon cinnamon roll" style="margin-left:30px;width:79px;height:73px;background:radial-gradient(circle,#e39a5c,#b5602a);"></div>
    <p class="price" style="margin-left:16px;">$ 00.0</p>
  </div>

  <h2 class="item-name" style="left:28px;top:650px;">Beverages</h2>
  <div role="img" aria-label="Cartoon cup of steaming coffee" style="left:48px;top:701px;width:83px;height:121px;border-radius:40%;background:linear-gradient(180deg,#e9dcc6,#ffffff 60%,#e2e2e2);"></div>
  <div role="img" aria-label="Cartoon milk carton" style="left:143px;top:727px;width:69px;height:118px;background:linear-gradient(180deg,#ffffff,#e6e6e6);"></div>
  <p class="drink" style="left:255px;top:697px;">Coffee</p>
  <p class="drink-price" style="left:450px;top:697px;">$ 00.0</p>
  <p class="drink" style="left:255px;top:748px;">Soda</p>
  <p class="drink-price" style="left:450px;top:748px;">$ 00.0</p>
  <p class="drink" style="left:255px;top:801px;">Milk</p>
  <p class="drink-price" style="left:450px;top:801px;">$ 00.0</p>
</main>
</body>
</html>
```